依頼詳細
■デザインのみになります。コーディング・設置は必要ありません。

ターゲットの方々が経営者や弁護士・医師の方々ですので、シックな雰囲気や高級感のあるテイストを希望しています。あまりごちゃごちゃしない方がいいです。そしてPC表示とスマートフォン表示は別のものを用意していただきたいと思っています。その辺りは以下のサイトを参照してください。

https://ka-gakuin.example/lp1/

ファッション系のサービスなので、デザインにも、そこそここだわりたいと思っています。指標となるデザインは以下を参照してください。このようなテイストが個人的に好みです。あくまで参考程度に。

https://www.verdalune.example/
https://www.shokumalink.example/user/landing/general01
https://shigoto-meijin.example/

それではみなさんからのご提案を楽しみにしております。どうぞ宜しくお願いいたします。※デザインのみになります。コーディングは必要ありません。
サイトURL
http://kiriharada.example/
ページ数
5ページ
希望イメージ
シンプル 複雑
単色 カラフル
暗い 明るい
日常 高級
遊び心 厳粛
未来的 伝統的
女性的 男性的
希望する色
青系、茶系、グレー系
納品ファイル
• フォトショップ形式 (.psd)
• PNG形式 (.png)
補足説明
・ホームページとスマートフォンでデザインが最適化されることを望んでいます。
・原稿は「添付ファイル」を参照してください。
・写真素材はこちらからダウンロードをお願いします。
http://22.filebako.example/0617-x7k29d41m3p8q05r6t2w9y4z8c1v7n3b5
■LPは縦長の1ページでお願いします
■文章量は添付ファイルをご確認ください
■ページ数が5ページとなっていますが、制作は縦長の1ページでお願いします。それなりに文章量がありますので、5ページという形で表現しています。
写真素材は以下からダウンロードしてください。http://26.filebako.example/0624-h4j8l2n6p0r3t7v1x5z9b2d6f0g4k8m1q(ギガファイル便6月24日まで)
■ 選んだ理由

センスの良さが際立っていました。ファッション分野のLPなので、細部にまで満足のいくデザインに巡り会えたのはとてもありがたいことだと感じています。

■ 提案者全員のお礼・コメント

この度は優れたデサインを多数ご提案いただきまして、誠にありがとうございました。レベルが高く、選ぶのが大変でしたがとても満足のいくコンペになりました。また機会がありましたら宜しくお願いいたします。

```html
<!DOCTYPE html>
<html lang="ja">
<head>
<meta charset="utf-8">
<title>Atelier Kirihara | 経営者のための専属スタイリストサービス</title>
<link rel="stylesheet" href="https://fonts.googleapis.com/css2?family=Noto+Sans+JP:wght@400;500;700&family=Noto+Serif+JP:wght@400;600;700&family=Playfair+Display:ital,wght@1,400;1,600&display=swap">
<style>
:root{
  --ink:#222222;
  --ink-soft:#555555;
  --paper:#ffffff;
  --mist:#f1f1f1;
  --band:#262626;
  --gold:#c9a15e;
  --accent:#c2412d;
  --ghost:rgba(0,0,0,.06);
  --line:#d6d6d6;
}
*{margin:0;padding:0;box-sizing:border-box}
html,body{width:1200px;height:4368px;overflow:hidden}
body{background:var(--paper);color:var(--ink);font-family:"Noto Sans JP",sans-serif;position:relative}
.abs{position:absolute}
.section{position:absolute;left:0;width:1200px}
.ghost{position:absolute;left:0;width:1200px;text-align:center;font-family:"Playfair Display",serif;font-style:italic;font-size:130px;color:var(--ghost);line-height:1;white-space:nowrap}
.heading{position:absolute;left:0;width:1200px;text-align:center}
.heading .en{font-family:"Playfair Display",serif;font-style:italic;font-size:42px;color:var(--ink);line-height:1.1}
.heading .ja{font-size:13px;color:var(--ink-soft);margin-top:6px;letter-spacing:.1em}

/* hero */
.hero{top:0;height:540px;background:linear-gradient(100deg,#9a958c 0%,#bdb5a8 40%,#d8d2c7 70%,#a49c90 100%)}
.brand{top:28px;left:0;width:1200px;text-align:center;color:var(--paper);font-family:"Noto Serif JP",serif;font-size:19px;font-weight:600;letter-spacing:.08em}
.hero-title{top:180px;left:64px;color:var(--paper);font-size:40px;font-weight:700;line-height:1.45;letter-spacing:.04em;text-shadow:0 2px 8px rgba(0,0,0,.25)}
.hero-lead{top:312px;left:64px;color:var(--paper);font-size:19px;font-weight:500;line-height:1.7;text-shadow:0 2px 6px rgba(0,0,0,.25)}
.hero-lead em{font-style:normal;color:var(--accent);font-size:24px;font-weight:700}
.hero-btn{top:440px;left:64px;width:220px;height:48px;background:var(--paper);color:var(--ink);font-size:14px;display:flex;align-items:center;justify-content:center;gap:12px}

/* profile */
.profile{top:540px;height:450px;background:var(--mist)}
.book-photo{top:140px;left:130px;width:340px;height:260px;background:linear-gradient(135deg,#2d3448,#6c7894 55%,#e8e6e2)}
.profile-card{top:222px;left:500px;width:420px;background:var(--paper);padding:22px 30px 18px}
.profile-card .role{font-size:15px;color:var(--ink-soft)}
.profile-card .name{font-family:"Noto Serif JP",serif;font-size:32px;font-weight:700;margin-top:4px;letter-spacing:.08em;line-height:1.3}
.profile-card .tags{font-size:11px;color:#888;margin-top:6px}
.person-photo{top:150px;left:930px;width:130px;height:260px;background:linear-gradient(180deg,#d9d9d9,#3a3d45 45%,#2a2c33)}

/* cta */
.cta{height:210px;background:var(--band)}
.cta-box{top:58px;left:340px;width:520px;height:100px;border:1px solid rgba(255,255,255,.7);color:var(--paper);font-size:28px;font-weight:600;line-height:1.35;display:flex;align-items:center;padding-left:60px}
.cta-seal{top:52px;left:820px;width:112px;height:112px;border-radius:50%;background:var(--gold);color:var(--paper);display:flex;flex-direction:column;align-items:center;justify-content:center;font-size:13px;line-height:1.2}
.cta-seal b{font-family:"Playfair Display",serif;font-size:36px;font-style:italic}

/* seminar */
.seminar-photo{top:1200px;height:360px;background:linear-gradient(90deg,#3b3330,#7a6d64 40%,#cfcac4 70%,#6a625c)}

/* troubles */
.troubles-bg{top:1560px;height:600px;background:var(--mist)}
.troubles-card{top:1460px;left:160px;width:880px;height:680px;background:var(--paper)}
.check-list{top:220px;left:70px;list-style:none}
.check-list li{font-size:17px;line-height:40px;display:flex;align-items:center;gap:12px}
.check-list svg{flex:none}
.suits-illust{top:210px;left:510px;width:300px;height:350px;background:linear-gradient(180deg,#f3f4f7,#bcc4d4 50%,#8d95a8)}
.troubles-note{top:610px;left:0;width:880px;text-align:center;font-size:13px;color:var(--ink-soft)}

/* reason */
.reason{top:2160px;height:800px;background:var(--mist)}
.reason-intro{top:170px;left:0;width:1200px;text-align:center;font-size:14px;line-height:2;color:var(--ink-soft)}
.reason-row{left:160px;width:880px;height:200px;background:var(--paper);display:flex}
.reason-row .photo{width:320px;height:200px;flex:none}
.reason-row .body{padding:30px 34px}
.reason-row h3{font-size:19px;font-weight:700;margin-bottom:14px;line-height:1.5}
.reason-row p{font-size:13px;line-height:1.9;color:var(--ink-soft)}

/* professional */
.pro{top:3180px;height:640px;background:var(--paper)}
.pro .ghost{text-align:left;left:-20px;top:40px;width:auto}
.pro-text{top:130px;left:160px;width:540px}
.pro-text h2{font-size:22px;font-weight:700;line-height:1.7;white-space:nowrap}
.pro-text h2 .num{font-family:"Playfair Display",serif;font-style:italic;color:var(--accent);font-size:50px;vertical-align:-4px;margin-right:4px}
.pro-text p{font-size:14px;line-height:2;color:var(--ink-soft);margin-top:22px}
.pro-photo{top:80px;left:740px;width:460px;height:520px;background:linear-gradient(120deg,#e8e6e2,#8c8f99 40%,#2f3441 70%,#d9d6d1)}

/* merit */
.merit{top:3820px;height:548px;background:var(--mist)}
.merit-card{top:200px;width:260px;height:320px;background:var(--paper);text-align:center;padding:26px 20px}
.merit-card .icon{width:90px;height:90px;border-radius:50%;margin:0 auto 18px}
.merit-card h3{font-size:14px;font-weight:700;margin-bottom:12px;white-space:nowrap}
.merit-card p{font-size:12px;line-height:1.9;color:var(--ink-soft);text-align:left}
</style>
</head>
<body>

<header class="section hero" role="img" aria-label="書斎でくつろぐスタイリストの写真">
  <div class="abs brand">Atelier Kirihara</div>
  <h1 class="abs hero-title">ファッションでブランディングを<br>加速させる方法とは？</h1>
  <p class="abs hero-lead">既に<em>5万名</em>以上が「センスのいい経営者」に変わった<br>経営者のための専属スタイリストサービス</p>
  <a class="abs hero-btn">お申込みはこちら
    <svg width="8" height="12" viewBox="0 0 8 12"><path d="M1 1l5 5-5 5" fill="none" stroke="#222" stroke-width="1.5"/></svg></a>
</header>

<section class="section profile">
  <div class="ghost" style="top:30px">Profile</div>
  <div class="heading" style="top:60px"><div class="en">Profile</div><div class="ja">プロフィール</div></div>
  <div class="abs book-photo" role="img" aria-label="著書の表紙写真"></div>
  <div class="abs profile-card">
    <div class="role">累計5万部以上の著書を持つスタイリスト</div>
    <div class="name">桐原 颯</div>
    <div class="tags">雑誌連載／テレビ出演／講演多数／企業研修</div>
  </div>
  <div class="abs person-photo" role="img" aria-label="スーツ姿のスタイリストの写真"></div>
</section>

<section class="section cta" style="top:990px">
  <div class="abs cta-box">初回カウンセリングの<br>お申込みはこちら</div>
  <div class="abs cta-seal"><span><b>3</b>名限定</span><span>Click</span></div>
</section>

<div class="section seminar-photo" role="img" aria-label="セミナーで講演するスタイリストの写真"></div>

<div class="section troubles-bg"></div>
<section class="abs troubles-card">
  <div class="ghost" style="top:50px;width:880px">Troubles</div>
  <div class="heading" style="top:90px;width:880px">
    <div class="en">Troubles</div>
    <div class="ja">日々のファッションにこんな悩みはありませんか？</div>
  </div>
  <ul class="abs check-list">
    <li><svg width="18" height="18" viewBox="0 0 18 18"><rect x="1" y="1" width="16" height="16" fill="none" stroke="#222"/><path d="M4 9l4 4 7-9" fill="none" stroke="#222" stroke-width="2"/></svg>ビジネスでのブランディングに力を入れたい</li>
    <li><svg width="18" height="18" viewBox="0 0 18 18"><rect x="1" y="1" width="16" height="16" fill="none" stroke="#222"/><path d="M4 9l4 4 7-9" fill="none" stroke="#222" stroke-width="2"/></svg>講演やセミナーなどで人前に立つことが増えてきた</li>
    <li><svg width="18" height="18" viewBox="0 0 18 18"><rect x="1" y="1" width="16" height="16" fill="none" stroke="#222"/><path d="M4 9l4 4 7-9" fill="none" stroke="#222" stroke-width="2"/></svg>メディアに出演することが増えてきた</li>
    <li><svg width="18" height="18" viewBox="0 0 18 18"><rect x="1" y="1" width="16" height="16" fill="none" stroke="#222"/><path d="M4 9l4 4 7-9" fill="none" stroke="#222" stroke-width="2"/></svg>今の立場にふさわしいファッションに変わりたい</li>
    <li><svg width="18" height="18" viewBox="0 0 18 18"><rect x="1" y="1" width="16" height="16" fill="none" stroke="#222"/><path d="M4 9l4 4 7-9" fill="none" stroke="#222" stroke-width="2"/></svg>信頼される見た目に変わりたい</li>
    <li><svg width="18" height="18" viewBox="0 0 18 18"><rect x="1" y="1" width="16" height="16" fill="none" stroke="#222"/><path d="M4 9l4 4 7-9" fill="none" stroke="#222" stroke-width="2"/></svg>自分のセンスに自信がない</li>
    <li><svg width="18" height="18" viewBox="0 0 18 18"><rect x="1" y="1" width="16" height="16" fill="none" stroke="#222"/><path d="M4 9l4 4 7-9" fill="none" stroke="#222" stroke-width="2"/></svg>服選びは奥さんや店員さんに任せっぱなし</li>
    <li><svg width="18" height="18" viewBox="0 0 18 18"><rect x="1" y="1" width="16" height="16" fill="none" stroke="#222"/><path d="M4 9l4 4 7-9" fill="none" stroke="#222" stroke-width="2"/></svg>いつまでも魅力的な経営者でありたい</li>
  </ul>
  <div class="abs suits-illust" role="img" aria-label="スーツ姿の男性二人のイラスト"></div>
  <p class="abs troubles-note">ひとつでも当てはまる方はぜひファッションを見直してみてください。</p>
</section>

<section class="section reason">
  <div class="ghost" style="top:36px">Reason</div>
  <div class="heading" style="top:66px"><div class="en">Reason</div><div class="ja">服装を見直すことがビジネスに効く理由とは？</div></div>
  <p class="abs reason-intro">近年、ファッションは経営者の印象を大きく左右する要素として注目されています。<br>見た目が整うだけで信頼感が生まれ、仕事の成果にもつながります。<br>だからこそ経営者の服装選びには専門家の視点が欠かせないのです。</p>
  <div class="abs reason-row" style="top:320px">
    <div class="photo" role="img" aria-label="ジャケットを選ぶ様子の写真" style="background:linear-gradient(120deg,#3a3f4c,#8a8378 60%,#d7d1c8)"></div>
    <div class="body"><h3>他社との差別化にパーソナルブランディングは不可欠</h3><p>商品やサービスだけで差をつけるのは難しい時代です。経営者自身の印象を磨くことが、選ばれる理由になります。見た目はその第一歩です。</p></div>
  </div>
  <div class="abs reason-row" style="top:540px">
    <div class="photo" role="img" aria-label="スタイリストが服を合わせる写真" style="background:linear-gradient(120deg,#2b2e36,#6f7482 55%,#d9d5cf)"></div>
    <div class="body"><h3>最短距離で「センスのいい経営者」になる方法とは？</h3><p>自己流で服を選ぶと時間も費用もかかります。プロのスタイリストに任せれば、短期間で自分に合う装いが身につきます。</p></div>
  </div>
</section>

<section class="section cta" style="top:2960px">
  <div class="abs cta-box">初回カウンセリングの<br>お申込みはこちら</div>
  <div class="abs cta-seal"><span><b>3</b>名限定</span><span>Click</span></div>
</section>

<section class="section pro">
  <div class="ghost">Professional</div>
  <div class="abs pro-text">
    <h2><span class="num">300</span>人以上の経営者のブランディングを<br>手掛けたファッションのプロ</h2>
    <p>これまで多くの経営者や専門職の方の装いを担当してきました。立場や業種、体型に合わせた服選びで、一人ひとりの魅力を引き出します。</p>
    <p>忙しい方でも無理なく続けられるよう、買い物同行から手持ち服の見直しまで丁寧にサポートいたします。</p>
  </div>
  <div class="abs pro-photo" role="img" aria-label="談笑するスタイリストと経営者の写真"></div>
</section>

<section class="section merit">
  <div class="ghost" style="top:26px">Merit</div>
  <div class="heading" style="top:56px"><div class="en">Merit</div><div class="ja">スタイリストを付けるメリットとは？</div></div>
  <div class="abs merit-card" style="left:160px">
    <div class="icon" role="img" aria-label="ブランディングを表すアイコン" style="background:#e7c25e"></div>
    <h3>パーソナルブランディングができる</h3>
    <p>立場にふさわしい装いで第一印象が変わり、信頼される経営者像を自然に伝えられるようになります。</p>
  </div>
  <div class="abs merit-card" style="left:470px">
    <div class="icon" role="img" aria-label="時間節約を表す時計のアイコン" style="background:#d9dde4"></div>
    <h3>時間が節約できる</h3>
    <p>服選びに悩む時間がなくなり、本業に集中できます。必要な服だけを効率よく揃えられます。</p>
  </div>
  <div class="abs merit-card" style="left:780px">
    <div class="icon" role="img" aria-label="自信の向上を表すアイコン" style="background:#8fb6d6"></div>
    <h3>セルフイメージが向上する</h3>
    <p>似合う服を着ることで自信が生まれ、人前に立つ場面でも堂々と振る舞えるようになります。</p>
  </div>
</section>

</body>
</html>
```